T.R.L (Tidal Resonance Lifting) is a form of energy healing that raises the vibration of the DNA so that it releases old energy patterns that no longer serve you. This allows the body to remember its natural ability to heal itself perfectly.

The energy is called in telepathically from the Acturians, the dolphins, the platinum ray and the Octahedron.

I would like a logo that incorporates all of these moadlities.

I will also require help with setting up my facebook page and website but until these are setup I cannot include the details so space will need to be saved for this on the business card

Target Market(s)

Alternative health

Industry/Entity Type

Business

Logo Text

T.R.L

Requirements
Must have
• Colors of the platinum ray. I have drafted the below as to what I would like it to say on it:-

Business Card –
Front:-
Taking you to a higher vibration
Mabel Thornby
Tidal Resonance Lifting Facilitator
www.quorvintel.example
+(61) 412 735 289 mabelthornby4471@quorvintel.example

Back:-
Appointments
For:-
Date: Time:
Location:

```html
<!DOCTYPE html>
<html lang="en">
<head>
<meta charset="utf-8">
<title>Mabel Thornby – Business Card</title>
<link rel="stylesheet" href="https://fonts.googleapis.com/css2?family=Marcellus&family=Raleway:wght@200;300&family=Lora:wght@700&display=swap">
<style>
  :root {
    --page-bg: #e9e6ee;
    --space-deep: #07060d;
    --space-navy: #141028;
    --nebula-violet: #7a3c8e;
    --nebula-magenta: #b45cb4;
    --nebula-glow: #f1dcf4;
    --platinum: #e6e3ee;
    --lavender: #c7a8d4;
    --field-fill: #cfb6d6;
    --field-edge: #efe6f2;
    --text-white: #ffffff;
    --text-soft: #d9d3e3;
  }
  * { box-sizing: border-box; margin: 0; padding: 0; }
  html, body { width: 1200px; height: 960px; overflow: hidden; }
  body {
    background: var(--page-bg);
    position: relative;
    font-family: "Raleway", "Century Gothic", sans-serif;
  }
  .card {
    position: absolute;
    left: 220px;
    width: 760px;
    height: 434px;
    border-radius: 6px;
    overflow: hidden;
    background: var(--space-deep);
    box-shadow: 0 10px 30px rgba(30, 20, 50, 0.25);
  }
  .card--back { top: 31px; }
  .card--front { top: 495px; }

  .nebula {
    position: absolute;
    inset: 0;
  }
  .card--back .nebula {
    background:
      radial-gradient(ellipse 120px 90px at 250px 110px, var(--nebula-glow) 0%, rgba(241,220,244,0.6) 35%, transparent 75%),
      radial-gradient(ellipse 260px 160px at 230px 140px, var(--nebula-magenta) 0%, rgba(122,60,142,0.7) 40%, transparent 80%),
      radial-gradient(ellipse 420px 260px at 260px 140px, rgba(60,40,110,0.7) 0%, transparent 80%),
      linear-gradient(160deg, var(--space-navy), var(--space-deep) 70%);
  }
  .card--front .nebula {
    background:
      radial-gradient(circle 70px at 200px 135px, rgba(255,255,255,0.85) 0%, transparent 80%),
      radial-gradient(circle 80px at 560px 190px, rgba(255,255,255,0.8) 0%, transparent 80%),
      radial-gradient(ellipse 170px 110px at 260px 190px, var(--nebula-glow) 0%, rgba(180,92,180,0.75) 45%, transparent 85%),
      radial-gradient(ellipse 320px 200px at 240px 230px, var(--nebula-violet) 0%, rgba(60,40,110,0.6) 55%, transparent 90%),
      linear-gradient(160deg, var(--space-navy), var(--space-deep) 70%);
  }

  /* Front */
  .tagline {
    position: absolute;
    top: 32px;
    left: 0;
    width: 100%;
    text-align: center;
    font-family: "Marcellus", "Optima", serif;
    font-size: 25px;
    letter-spacing: 2px;
    color: var(--text-white);
  }
  .art {
    position: absolute;
    border-radius: 50%;
  }
  .art--guide {
    left: 160px; top: 88px; width: 84px; height: 104px;
    background: radial-gradient(ellipse at 45% 40%, #c9bcd6, #6f5f85 80%);
    opacity: 0.85;
  }
  .art--dolphin {
    left: 515px; top: 148px; width: 84px; height: 110px;
    background: radial-gradient(ellipse at 50% 40%, #cfc6da, #6f6488 80%);
    opacity: 0.85;
    border-radius: 45% 55% 50% 50%;
  }
  .brand {
    position: absolute;
    left: 300px; top: 122px;
    width: 160px;
    display: flex;
    align-items: center;
    justify-content: center;
    gap: 10px;
    font-family: "Marcellus", "Optima", serif;
    font-size: 30px;
    color: var(--platinum);
  }
  .brand__mark {
    width: 18px; height: 18px;
    border: 1.5px solid var(--platinum);
  }
  .holder {
    position: absolute;
    left: 160px; top: 222px;
    font-weight: 200;
    font-size: 46px;
    color: var(--text-soft);
  }
  .role {
    position: absolute;
    left: 190px; top: 290px;
    font-family: "Lora", "Bookman", serif;
    font-weight: 700;
    font-size: 17px;
    letter-spacing: 0.5px;
    color: var(--lavender);
  }
  .contact {
    position: absolute;
    font-weight: 300;
    font-size: 16px;
    color: var(--text-soft);
  }
  .contact--web { left: 36px; top: 340px; }
  .contact--phone { left: 228px; top: 340px; }
  .contact--mail { right: 36px; top: 386px; }

  /* Back */
  .appointments {
    position: absolute;
    right: 48px; top: 56px;
    font-weight: 300;
    font-size: 28px;
    color: var(--text-white);
  }
  .booking {
    position: absolute;
    left: 380px; top: 104px;
    width: 340px;
  }
  .booking__field { margin-bottom: 10px; }
  .booking__field--for { margin-bottom: 34px; }
  .booking__label {
    display: block;
    font-size: 14px;
    font-weight: 300;
    color: var(--text-soft);
    margin-bottom: 2px;
  }
  .booking__line {
    display: block;
    height: 28px;
    background: var(--field-fill);
    border: 1px solid var(--field-edge);
    box-shadow: 0 0 10px rgba(239, 230, 242, 0.6);
  }
</style>
</head>
<body>

  <section class="card card--back" aria-label="Business card back">
    <div class="nebula" role="img" aria-label="Purple space nebula with a bright burst of light"></div>
    <h2 class="appointments">Appointments</h2>
    <div class="booking">
      <div class="booking__field booking__field--for">
        <span class="booking__label">For:</span>
        <span class="booking__line"></span>
      </div>
      <div class="booking__field">
        <span class="booking__label">Date:</span>
        <span class="booking__line"></span>
      </div>
      <div class="booking__field">
        <span class="booking__label">Time:</span>
        <span class="booking__line"></span>
      </div>
      <div class="booking__field">
        <span class="booking__label">Location:</span>
        <span class="booking__line"></span>
      </div>
    </div>
  </section>

  <section class="card card--front" aria-label="Business card front">
    <div class="nebula" role="img" aria-label="Purple space nebula with glowing light bursts"></div>
    <p class="tagline">TAKING YOU TO A HIGHER VIBRATION</p>
    <div class="art art--guide" role="img" aria-label="Illustration of an Arcturian guide's head"></div>
    <div class="brand">
      <span class="brand__mark"></span>
      <span class="brand__name">T.R.L</span>
    </div>
    <div class="art art--dolphin" role="img" aria-label="Illustration of a leaping dolphin"></div>
    <h1 class="holder">Mabel Thornby</h1>
    <p class="role">Tidal Resonance Lifting Facilitator</p>
    <p class="contact contact--web">www.quorvintel.example</p>
    <p class="contact contact--phone">+(61) 412 735 289</p>
    <p class="contact contact--mail">mabelthornby4471@quorvintel.example</p>
  </section>

</body>
</html>
```